Brisk Hollow Builders Needs A Flyer

We need a flyer for our newest product "The Cedarlane Garden Workroom"

Here is some copy for the flyer:

1. More and more people everyday are working from home and finding it difficult to disconnect from home activities in order to focus on their work. They are also finding it very expensive to add on to their existing house for a quiet place. Our archatectually stunning, Cedarlane Garden Workroom is the answer. The office studio measures 16' wide and 10' deep. 160 Square feet of space.

Perfect for dozens of purposes. Home office, design studio, artist studio, home school office, reading room, craft studio, drafting room.

Features include:

- Steel Framing. 40-60% lighter then wood, higher strength to weight ratio, resistant to mold and fire and steel is the most recycled material on earth!
- Spray foam insulation. Cool in the summer and warm in the winter.
- HVAC Mini Split with wireless remote control and thermostat.
- 100% Off grid with enough solar and battery storage to run your entire office. No need to pay for an expensive electric installation.
- Flush fitting floor outlets to reduce wires.
- TV mount (Optional with pre-wired electric, HDMI, digital audio & Cat 6)
- Windows are tempered glass custom made by Morvik Glazing.
- Solar qualifies for a 26% tax credit. This is not a write-off rather it is a direct reduction on your tax obligation.
- Thousands of dollars less than adding onto your home.
- Custom color, siding, features available.

This beautiful back yard office is delivered 100% assembled and ready to enjoy on the day of delivery.

We ship nationwide from our factory in South Carolina. Give us a call anytime to speak to a designer and start your dream office today!

555-318-4027
info@BriskHollowBuilders.example

```html
<!DOCTYPE html>
<html lang="en">
<head>
<meta charset="utf-8">
<title>Brisk Hollow Builders – The Cedarlane Garden Workroom</title>
<link rel="stylesheet" href="https://fonts.googleapis.com/css2?family=Oswald:wght@400;500;600&family=Montserrat:wght@400;500;600;700&display=swap">
<style>
:root{
  --page:#eef0f2;
  --mint:#e3efe2;
  --green:#5ea34a;
  --green-dark:#3f8a35;
  --gold:#e0a92a;
  --navy:#1f2a33;
  --ink:#1c242b;
  --white:#ffffff;
  --paper:#f7f8fa;
}
*{box-sizing:border-box;margin:0;padding:0}
html,body{width:691px;height:1200px;overflow:hidden;background:var(--page)}
body{font-family:"Montserrat",Arial,sans-serif;color:var(--ink)}
.flyer{position:absolute;left:0;top:152px;width:691px;height:895px;background:var(--paper);overflow:hidden;box-shadow:0 4px 14px rgba(0,0,0,.18)}
.abs{position:absolute}
.hero{left:0;top:0;width:691px;height:300px;background:var(--mint)}
.hero-art{left:0;top:0}
.brand{left:30px;top:74px;display:flex;align-items:center;gap:8px;font-family:"Oswald",sans-serif;font-weight:600;font-size:22px;color:var(--gold);text-transform:uppercase;letter-spacing:.5px}
.brand-dot{width:14px;height:14px;border-radius:50%;background:var(--green)}
.headline{left:30px;top:162px;font-family:"Oswald",sans-serif;font-weight:500;font-size:34px;line-height:38px;text-transform:uppercase;color:var(--ink);letter-spacing:.3px}
.headline .gold{color:var(--gold)}
.headline .green{color:var(--green)}
.tagline{left:30px;top:244px;width:290px;font-size:10.2px;line-height:12.5px;font-weight:500;color:var(--ink)}
.band{left:0;top:306px;width:691px;height:164px;background:var(--green)}
.intro{left:30px;top:320px;width:262px;font-size:9.4px;line-height:14px;color:var(--white)}
.deliver{left:323px;top:316px;font-family:"Oswald",sans-serif;font-weight:500;font-size:25px;line-height:27px;color:var(--navy);text-transform:uppercase}
.deliver-sub{left:323px;top:373px;font-size:11.4px;font-weight:600;color:var(--white);letter-spacing:.4px;text-transform:uppercase}
.cta-box{left:320px;top:400px}
.cta-text{left:330px;top:410px;width:325px;text-align:center;font-size:9.6px;line-height:12px;color:var(--ink)}
.cta-text strong{display:block;margin-top:2px;font-family:"Oswald",sans-serif;font-weight:500;font-size:14px;text-transform:uppercase}
.features-tab{left:250px;top:470px}
.features-title{left:250px;top:474px;width:190px;text-align:center;font-family:"Oswald",sans-serif;font-size:21px;font-weight:500;color:var(--white);letter-spacing:.5px}
.feature-list{list-style:none;font-size:9.6px;line-height:11.8px;color:var(--ink)}
.feature-list li{position:relative;padding-left:24px;margin-bottom:6.5px}
.feature-list li svg{position:absolute;left:0;top:0}
.col-left{left:33px;top:530px;width:300px}
.col-right{left:368px;top:530px;width:270px}
.model{top:705px;height:118px;background:linear-gradient(180deg,#2a2f33 0%,#4a4f52 45%,#cfc6b8 70%,#3a3e41 100%);border-radius:2px}
.footer{left:0;top:835px;width:691px;height:60px}
.contact-title{left:30px;top:847px;font-family:"Oswald",sans-serif;font-size:15px;font-weight:500;color:var(--navy);text-transform:uppercase}
.contact-note{left:30px;top:866px;width:112px;font-size:6px;line-height:7px;color:var(--white);text-transform:uppercase}
.phone{left:156px;top:843px;display:flex;align-items:center;gap:8px;font-size:19px;font-weight:600;color:var(--white)}
.web{left:156px;top:869px;display:flex;align-items:center;gap:7px;font-size:8.8px;font-weight:600;color:var(--white)}
.addr{left:412px;top:849px;display:flex;align-items:center;gap:9px;font-size:9.2px;font-weight:600;color:var(--white)}
.mail{left:412px;top:868px;display:flex;align-items:center;gap:9px;font-size:9.2px;font-weight:600;color:var(--white)}
</style>
</head>
<body>
<main class="flyer">
  <section class="abs hero"></section>
  <svg class="abs hero-art" width="691" height="306" viewBox="0 0 691 306">
    <polygon points="370,0 392,0 352,300 330,300" fill="var(--gold)"/>
    <polygon points="384,0 400,0 364,300 348,300" fill="var(--green)"/>
    <defs><linearGradient id="scene" x1="0" y1="0" x2="0" y2="1">
      <stop offset="0" stop-color="#8fb4dc"/><stop offset=".35" stop-color="#4e6b3a"/>
      <stop offset=".55" stop-color="#5b5a55"/><stop offset=".8" stop-color="#6f8c3e"/><stop offset="1" stop-color="#4f7a2e"/>
    </linearGradient></defs>
    <polygon points="400,0 691,0 691,300 364,300" fill="url(#scene)" role="img" aria-label="Photo of the garden workroom with roof solar panels in a landscaped back yard"/>
    <rect x="0" y="300" width="691" height="6" fill="var(--gold)"/>
  </svg>

  <div class="abs brand"><span class="brand-dot"></span>Brisk Hollow Builders</div>
  <h1 class="abs headline">The <span class="gold">Cedarlane</span><br><span class="green">Garden</span> Workroom</h1>
  <p class="abs tagline">Perfect for dozens of purposes. Home office, design studio, artist studio, home school office, reading room, craft studio, drafting room.</p>

  <section class="abs band"></section>
  <p class="abs intro">More and more people everyday are working from home and finding it difficult to disconnect from home activities in order to focus on their work. They are also finding it very expensive to add on to their existing house for a quiet place. Our architecturally stunning, Cedarlane Garden Workroom is the answer. The office studio measures 16' wide and 10' deep. 160 Square feet of space.</p>
  <h2 class="abs deliver">This beautiful back yard office<br>is delivered 100% assembled</h2>
  <p class="abs deliver-sub">And ready to enjoy on the day of delivery.</p>
  <svg class="abs cta-box" width="350" height="64" viewBox="0 0 350 64"><polygon points="0,0 330,0 345,64 0,64" fill="var(--white)"/></svg>
  <p class="abs cta-text">We ship nationwide from our factory in South Carolina.<br>Give us a call anytime to speak to a designer<strong>And start your dream office today!</strong></p>

  <svg class="abs features-tab" width="190" height="38" viewBox="0 0 190 38"><polygon points="0,0 190,0 168,38 22,38" fill="var(--navy)"/></svg>
  <h3 class="abs features-title">FEATURES</h3>

  <ul class="abs feature-list col-left">
    <li><svg width="14" height="14" viewBox="0 0 14 14"><circle cx="7" cy="7" r="6" fill="none" stroke="var(--green)" stroke-width="2"/><path d="M4 7l2 2 4-4" stroke="var(--green)" stroke-width="1.6" fill="none"/></svg>Steel Framing. 40-60% lighter then wood, higher strength to weight ratio, resistant to mold and fire and steel is the most recycled material on earth!</li>
    <li><svg width="14" height="14" viewBox="0 0 14 14"><circle cx="7" cy="7" r="6" fill="none" stroke="var(--green)" stroke-width="2"/><path d="M4 7l2 2 4-4" stroke="var(--green)" stroke-width="1.6" fill="none"/></svg>Spray foam insulation. Cool in the summer and warm in the winter.</li>
    <li><svg width="14" height="14" viewBox="0 0 14 14"><circle cx="7" cy="7" r="6" fill="none" stroke="var(--green)" stroke-width="2"/><path d="M4 7l2 2 4-4" stroke="var(--green)" stroke-width="1.6" fill="none"/></svg>HVAC Mini Split with wireless remote control and thermostat.</li>
    <li><svg width="14" height="14" viewBox="0 0 14 14"><circle cx="7" cy="7" r="6" fill="none" stroke="var(--green)" stroke-width="2"/><path d="M4 7l2 2 4-4" stroke="var(--green)" stroke-width="1.6" fill="none"/></svg>100% Off grid with enough solar and battery storage to run your entire office. No need to pay for an expensive electric installation.</li>
    <li><svg width="14" height="14" viewBox="0 0 14 14"><circle cx="7" cy="7" r="6" fill="none" stroke="var(--green)" stroke-width="2"/><path d="M4 7l2 2 4-4" stroke="var(--green)" stroke-width="1.6" fill="none"/></svg>Flush fitting floor outlets to reduce wires.</li>
  </ul>
  <ul class="abs feature-list col-right">
    <li><svg width="14" height="14" viewBox="0 0 14 14"><circle cx="7" cy="7" r="6" fill="none" stroke="var(--green)" stroke-width="2"/><path d="M4 7l2 2 4-4" stroke="var(--green)" stroke-width="1.6" fill="none"/></svg>TV mount (Optional with pre-wired electric, HDMI, digital audio &amp; Cat 6)</li>
    <li><svg width="14" height="14" viewBox="0 0 14 14"><circle cx="7" cy="7" r="6" fill="none" stroke="var(--green)" stroke-width="2"/><path d="M4 7l2 2 4-4" stroke="var(--green)" stroke-width="1.6" fill="none"/></svg>Windows are tempered glass custom made by Morvik Glazing.</li>
    <li><svg width="14" height="14" viewBox="0 0 14 14"><circle cx="7" cy="7" r="6" fill="none" stroke="var(--green)" stroke-width="2"/><path d="M4 7l2 2 4-4" stroke="var(--green)" stroke-width="1.6" fill="none"/></svg>Solar qualifies for a 26% tax credit. This is not a write-off rather it is a direct reduction on your tax obligation.</li>
    <li><svg width="14" height="14" viewBox="0 0 14 14"><circle cx="7" cy="7" r="6" fill="none" stroke="var(--green)" stroke-width="2"/><path d="M4 7l2 2 4-4" stroke="var(--green)" stroke-width="1.6" fill="none"/></svg>Thousands of dollars less than adding onto your home.</li>
    <li><svg width="14" height="14" viewBox="0 0 14 14"><circle cx="7" cy="7" r="6" fill="none" stroke="var(--green)" stroke-width="2"/><path d="M4 7l2 2 4-4" stroke="var(--green)" stroke-width="1.6" fill="none"/></svg>Custom color, siding, features available.</li>
  </ul>

  <div class="abs model" style="left:45px;width:195px" role="img" aria-label="Rendering of the workroom exterior with glass doors, angled view from the left"></div>
  <div class="abs model" style="left:255px;width:180px" role="img" aria-label="Rendering of the workroom front with glass doors and furnished interior"></div>
  <div class="abs model" style="left:448px;width:195px" role="img" aria-label="Rendering of the workroom exterior, angled view from the right"></div>

  <svg class="abs footer" width="691" height="60" viewBox="0 0 691 60">
    <rect width="691" height="60" fill="var(--green)"/>
    <polygon points="386,0 691,0 691,60 368,60" fill="var(--navy)"/>
    <polygon points="400,0 691,0 691,60 382,60" fill="var(--gold)"/>
  </svg>
  <p class="abs contact-title">Contact us today</p>
  <p class="abs contact-note">To discuss our highly rewarding partner programs.</p>
  <p class="abs phone"><svg width="11" height="11" viewBox="0 0 24 24"><path d="M6.6 10.8a15 15 0 006.6 6.6l2.2-2.2c.3-.3.7-.4 1-.2 1.1.4 2.3.6 3.6.6.6 0 1 .4 1 1V20c0 .6-.4 1-1 1C10.6 21 3 13.4 3 4c0-.6.4-1 1-1h3.5c.6 0 1 .4 1 1 0 1.3.2 2.5.6 3.6.1.3 0 .7-.2 1z" fill="var(--white)"/></svg>555-318-4027</p>
  <p class="abs web"><svg width="11" height="11" viewBox="0 0 24 24"><circle cx="12" cy="12" r="9" fill="none" stroke="var(--white)" stroke-width="2"/><path d="M3 12h18M12 3c3 3 3 15 0 18M12 3c-3 3-3 15 0 18" fill="none" stroke="var(--white)" stroke-width="1.6"/></svg>www.briskhollowbuilders.example</p>
  <p class="abs addr"><svg width="9" height="12" viewBox="0 0 18 24"><path d="M9 0a9 9 0 00-9 9c0 7 9 15 9 15s9-8 9-15a9 9 0 00-9-9zm0 12a3 3 0 110-6 3 3 0 010 6z" fill="var(--white)"/></svg>2740 Larkspur Ridge Rd, Fairmont, SC 29000</p>
  <p class="abs mail"><svg width="11" height="9" viewBox="0 0 22 16"><rect width="22" height="16" rx="1" fill="var(--white)"/><path d="M1 1l10 8 10-8" fill="none" stroke="var(--gold)" stroke-width="1.8"/></svg>info@BriskHollowBuilders.example</p>
</main>
</body>
</html>
```